Postcard Design

The business Logo is 'Verdo' it is grass cutting and maintenance. It will offer grass cutting with stripes including edging. Other services include decking/fencing maintenance, lawn treatment and patio/drive cleaning...... prices start from £10 to include front and rear lawns, Regular cuts or a one off tidy. private and commercial. Contracts welcome.
call 01642583106 or 07474829150 for a free quote.
one of the pics that i have sent is the logo (obviously it would need to be tidied up and neater) that is just rough. The other pic is one of pella cards templates but is the one that is the preferred out of all of them. If it could be similar to that with the logo on would be great.
a before (long scruffy grass) and after (neat Lawn) half and half of the postcard would be great.

Target Market(s)

Middle class home owners.

Industry/Entity Type

Business

Requirements
Must have
• The 'Verdo' logo
Nice to have
• we have a lot of junk mail posted in this area and a lot just gets put in the bin so could you make it eye catching.

```html
<!DOCTYPE html>
<html lang="en">
<head>
<meta charset="utf-8">
<title>Verdo – Grass Cutting and Maintenance Postcard</title>
<link rel="stylesheet" href="https://fonts.googleapis.com/css2?family=Oswald:wght@600&family=Jost:wght@400;600&display=swap">
<style>
  :root {
    --page-bg: #e9e6e1;
    --grass-dark: #3f7f1f;
    --grass-mid: #5a9e2c;
    --grass-light: #78b43a;
    --panel: #2b3327;
    --panel-text: #f2f2f2;
    --logo-text: #ececec;
    --price-badge: #bdbdc0;
    --price-text: #111111;
  }
  * { margin: 0; padding: 0; box-sizing: border-box; }
  html, body {
    width: 1200px;
    height: 901px;
    overflow: hidden;
    background: var(--page-bg);
  }
  .postcard {
    position: absolute;
    left: 30px;
    top: 10px;
    width: 1140px;
    height: 880px;
    overflow: hidden;
  }
  .grass-texture {
    position: absolute;
    inset: 0;
    background:
      radial-gradient(ellipse at 30% 40%, var(--grass-light) 0%, transparent 60%),
      radial-gradient(ellipse at 75% 70%, var(--grass-light) 0%, transparent 55%),
      linear-gradient(160deg, var(--grass-mid), var(--grass-dark));
  }
  .tagline {
    position: absolute;
    left: 171px;
    top: 74px;
    width: 754px;
    font-family: "Oswald", sans-serif;
    font-weight: 600;
    font-size: 52px;
    line-height: 1;
    color: var(--logo-text);
    text-align: center;
    letter-spacing: -0.5px;
    white-space: nowrap;
  }
  .brand-name {
    position: absolute;
    left: 169px;
    top: 126px;
    width: 756px;
    font-family: "Oswald", sans-serif;
    font-weight: 600;
    font-size: 238px;
    line-height: 1;
    color: var(--logo-text);
    text-align: center;
    letter-spacing: 14px;
  }
  .services {
    position: absolute;
    left: 0;
    top: 473px;
    width: 612px;
    height: 177px;
    background: var(--panel);
    list-style: none;
    padding: 40px 0 0 34px;
  }
  .services li {
    display: flex;
    align-items: center;
    height: 40px;
    font-family: "Jost", sans-serif;
    font-weight: 600;
    font-size: 28px;
    color: var(--panel-text);
    letter-spacing: 0.6px;
  }
  .tick-box {
    width: 22px;
    height: 22px;
    margin-right: 20px;
    flex: none;
  }
  .price-badge {
    position: absolute;
    left: 458px;
    top: 581px;
    width: 158px;
    height: 158px;
  }
  .price-badge span {
    position: absolute;
    inset: 0;
    display: flex;
    align-items: center;
    justify-content: center;
    font-family: "Jost", sans-serif;
    font-weight: 400;
    font-size: 66px;
    color: var(--price-text);
  }
  .contact-band {
    position: absolute;
    left: 0;
    top: 755px;
    width: 1140px;
    height: 106px;
    background: var(--panel);
    text-align: center;
    font-family: "Jost", sans-serif;
    font-weight: 400;
    font-size: 30px;
    line-height: 40px;
    color: var(--panel-text);
    padding-top: 12px;
    letter-spacing: 0.4px;
  }
</style>
</head>
<body>
  <div class="postcard">
    <div class="grass-texture" role="img" aria-label="Close-up photograph of a neat green lawn filling the card"></div>

    <p class="tagline">GRASS CUTTING AND MAINTENANCE</p>
    <p class="brand-name">VERDO</p>

    <ul class="services">
      <li>
        <svg class="tick-box" viewBox="0 0 22 22" aria-hidden="true">
          <rect width="22" height="22" rx="4" fill="#f2f2f2"/>
          <path d="M5 11.5l4 4 8-9" fill="none" stroke="#2b3327" stroke-width="3" stroke-linecap="round" stroke-linejoin="round"/>
        </svg>
        decking/fencing maintenance
      </li>
      <li>
        <svg class="tick-box" viewBox="0 0 22 22" aria-hidden="true">
          <rect width="22" height="22" rx="4" fill="#f2f2f2"/>
          <path d="M5 11.5l4 4 8-9" fill="none" stroke="#2b3327" stroke-width="3" stroke-linecap="round" stroke-linejoin="round"/>
        </svg>
        lawn treatment
      </li>
      <li>
        <svg class="tick-box" viewBox="0 0 22 22" aria-hidden="true">
          <rect width="22" height="22" rx="4" fill="#f2f2f2"/>
          <path d="M5 11.5l4 4 8-9" fill="none" stroke="#2b3327" stroke-width="3" stroke-linecap="round" stroke-linejoin="round"/>
        </svg>
        patio/drive cleaning
      </li>
    </ul>

    <div class="price-badge">
      <svg viewBox="0 0 158 158" width="158" height="158" aria-hidden="true">
        <path d="M79 0H158V79A79 79 0 0 1 79 158A79 79 0 0 1 0 79A79 79 0 0 1 79 0Z" fill="var(--price-badge)"/>
      </svg>
      <span>£10</span>
    </div>

    <div class="contact-band">
      <p>Contracts welcome</p>
      <p>call 01642583106 or 07474829150 for a free quote</p>
    </div>
  </div>
</body>
</html>
```